business card for a shoe shop

we would like a business card for a family owned shoe shop.
With this information included.
Darnell's Shoe Store
Family owned since 1947

then on other side
Darnell's Shoe Store
Footwear fitting specialist
Phone: 9187 2630
218 Quarry St, Fernleigh Downs 3187
(cnr. Hartwick Rd and Quarry St)
darnellshoes218@examplemail.com
if could incorporate the purple color on card i have attached.

```html
<!DOCTYPE html>
<html lang="en">
<head>
<meta charset="utf-8">
<title>Darnell's Shoe Store – Business Card</title>
<link rel="stylesheet" href="https://fonts.googleapis.com/css2?family=Arimo:wght@400;700&display=swap">
<style>
  :root {
    --purple: #8b4ef2;
    --purple-light: #9d62f8;
    --ink: #2b2b2b;
    --paper: #ffffff;
    --backdrop: #e9e7ee;
  }
  * { box-sizing: border-box; margin: 0; padding: 0; }
  html, body { width: 1200px; height: 874px; overflow: hidden; }
  body {
    background: var(--backdrop);
    font-family: "Arimo", Arial, sans-serif;
    position: relative;
  }
  .card {
    position: absolute;
    left: 290px;
    width: 620px;
    height: 354px;
    border-radius: 22px;
    overflow: hidden;
    box-shadow: 0 10px 28px rgba(40, 20, 80, 0.18);
  }
  .card--front {
    top: 62px;
    background: linear-gradient(135deg, var(--purple) 0%, var(--purple-light) 100%);
    display: flex;
    align-items: center;
    justify-content: center;
  }
  .card--back { top: 458px; background: var(--paper); }

  .brand { text-align: center; }
  .brand__name {
    font-weight: 700;
    font-size: 48px;
    line-height: 1.0;
    letter-spacing: 1px;
    text-transform: uppercase;
  }
  .card--front .brand__name { color: var(--paper); }
  .brand__tagline {
    display: flex;
    align-items: center;
    gap: 8px;
    margin-top: 8px;
    font-size: 20px;
  }
  .brand__tagline::before,
  .brand__tagline::after {
    content: "";
    flex: 1;
    height: 1px;
    background: currentColor;
    opacity: 0.8;
  }
  .card--front .brand__tagline { color: var(--paper); }

  .back__swoosh { position: absolute; left: 0; bottom: 0; width: 620px; height: 354px; }

  .back__brand {
    position: absolute;
    left: 44px;
    top: 92px;
    width: 250px;
  }
  .back__brand .brand__name { color: var(--purple); font-size: 36px; }
  .back__brand .brand__tagline { color: var(--ink); font-size: 15px; font-style: italic; margin-top: 6px; }

  .back__divider {
    position: absolute;
    left: 318px;
    top: 80px;
    width: 1px;
    height: 140px;
    background: var(--purple);
  }

  .contact {
    position: absolute;
    left: 338px;
    top: 96px;
    list-style: none;
    color: var(--ink);
  }
  .contact__item {
    display: flex;
    align-items: flex-start;
    gap: 8px;
    font-size: 12.5px;
    line-height: 1.35;
    margin-bottom: 8px;
  }
  .contact__item--phone { font-size: 24px; line-height: 1; }
  .contact__icon { width: 14px; height: 14px; flex: none; fill: var(--purple); margin-top: 1px; }
  .contact__item--phone .contact__icon { margin-top: 4px; }
</style>
</head>
<body>
  <section class="card card--front" aria-label="Card front">
    <div class="brand">
      <div class="brand__name">Darnell's<br>Shoe Store</div>
      <div class="brand__tagline">Family owned since 1947</div>
    </div>
  </section>

  <section class="card card--back" aria-label="Card back">
    <svg class="back__swoosh" viewBox="0 0 620 354" aria-hidden="true">
      <path d="M0 240 C 40 300, 300 320, 620 330 L620 354 L0 354 Z" fill="var(--purple-light)"/>
    </svg>

    <div class="brand back__brand">
      <div class="brand__name">Darnell's<br>Shoe Store</div>
      <div class="brand__tagline">Footwear fitting specialist</div>
    </div>

    <div class="back__divider"></div>

    <ul class="contact">
      <li class="contact__item contact__item--phone">
        <svg class="contact__icon" viewBox="0 0 24 24"><path d="M6.6 10.8a15.1 15.1 0 0 0 6.6 6.6l2.2-2.2c.3-.3.7-.4 1-.2 1.1.4 2.3.6 3.6.6.6 0 1 .4 1 1V20c0 .6-.4 1-1 1A17 17 0 0 1 3 4c0-.6.4-1 1-1h3.5c.6 0 1 .4 1 1 0 1.3.2 2.5.6 3.6.1.3 0 .7-.2 1z"/></svg>
        <span>9187 2630</span>
      </li>
      <li class="contact__item">
        <svg class="contact__icon" viewBox="0 0 24 24"><path d="M2 5h20v14H2z M2 5l10 8 10-8" fill="none" stroke="var(--purple)" stroke-width="2.2"/></svg>
        <span>darnellshoes218@examplemail.com</span>
      </li>
      <li class="contact__item">
        <svg class="contact__icon" viewBox="0 0 24 24"><path d="M12 2a7 7 0 0 0-7 7c0 5 7 13 7 13s7-8 7-13a7 7 0 0 0-7-7zm0 9.5A2.5 2.5 0 1 1 12 6.5a2.5 2.5 0 0 1 0 5z"/></svg>
        <span>218 Quarry St, Fernleigh Downs 3187<br>(cnr. Hartwick Rd and Quarry St)</span>
      </li>
    </ul>
  </section>
</body>
</html>
```